Tallowfen Capital Group - letterhead

We need a corporate letterhead template (word) and slide show template (PowerPoint) designed for our investment business Tallowfen Capital Group.

Tallowfen Capital Group manages a group of investments in Australia and are after a letterhead template and PowerPoint template that is both creative and professional in design.

Information to be included on the letterhead (word) template is as follows:

Level 4, 318 Marlow Road
Ashbury VIC 3147

t. 03 5127 6618

Please feel free to ask any questions.

Investment

```html
<!DOCTYPE html>
<html lang="en">
<head>
<meta charset="utf-8">
<title>Tallowfen Capital Group – Letterhead</title>
<link rel="stylesheet" href="https://fonts.googleapis.com/css2?family=Open+Sans:wght@400;600;700&display=swap">
<style>
  :root {
    --backdrop: #9a9ea3;
    --paper: #ffffff;
    --brand-blue: #0766a8;
    --band-grey: #b5b5b5;
    --address-grey: #a8a8a8;
    --ink: #2a2a2a;
  }
  * { box-sizing: border-box; margin: 0; padding: 0; }
  html, body {
    width: 1200px;
    height: 812px;
    overflow: hidden;
    background: var(--backdrop);
    font-family: "Open Sans", Arial, sans-serif;
  }
  .letterhead {
    position: absolute;
    left: 324px;
    top: 16px;
    width: 552px;
    height: 780px;
    background: var(--paper);
    box-shadow: 0 4px 14px rgba(0, 0, 0, 0.3);
    overflow: hidden;
  }
  .brand {
    position: absolute;
    left: 56px;
    top: 52px;
  }
  .brand-name {
    display: flex;
    align-items: center;
    gap: 8px;
    color: var(--brand-blue);
    font-size: 19px;
    font-weight: 600;
    letter-spacing: 0.2px;
  }
  .brand-mark {
    width: 12px;
    height: 12px;
    background: var(--brand-blue);
  }
  .address {
    margin-top: 10px;
    margin-left: 20px;
    color: var(--address-grey);
    font-size: 11px;
    font-weight: 700;
    line-height: 1.45;
  }
  .letter-body {
    position: absolute;
    left: 110px;
    right: 62px;
    top: 200px;
    color: var(--ink);
    font-size: 11.5px;
    line-height: 1.42;
  }
  .letter-body p { margin-bottom: 17px; }
  .salutation { margin-bottom: 10px !important; }
  .sign-off { margin-top: 14px; }
  .footer-band {
    position: absolute;
    left: 0;
    right: 0;
    bottom: 0;
    height: 26px;
    display: flex;
  }
  .footer-band .grey { width: 15%; background: var(--band-grey); }
  .footer-band .blue { flex: 1; background: var(--brand-blue); }
</style>
</head>
<body>
  <main class="letterhead">
    <header class="brand">
      <div class="brand-name"><span class="brand-mark"></span>Tallowfen Capital Group</div>
      <div class="address">
        Level 4, 318 Marlow Road<br>
        Ashbury VIC 3147<br>
        t. 03 5127 6618
      </div>
    </header>

    <section class="letter-body">
      <p class="salutation">Dear Sir/Madam,</p>
      <p>Lorem ipsum dolor sit amet, consectetur adipiscing elit. Nam dignissim scelerisque hendrerit. Nunc non tellus metus. Nulla dictum libero sem, sed elementum erat auctor sit amet. Aliquam quis urna luctus, porta orci nec, ultrices mi. Integer aliquet enim in ipsum egestas, nec varius purus sodales. Morbi enim mauris, iaculis et libero sed, rhoncus suscipit risus. Pellentesque vehicula libero ligula, at laoreet eros gravida nec. Suspendisse at nisi ac metus bibendum auctor. Cras ut arcu vel enim egestas iaculis sit amet a turpis. Quisque mattis tellus ut venenatis pulvinar. Nunc iaculis posuere dui sed euismod. Aenean gravida posuere metus, at blandit velit auctor a. In hac habitasse platea dictumst. Nullam venenatis ut ante sed ornare.</p>
      <p>Etiam justo arcu, tempor in leo a, convallis ultricies orci. Mauris tellus ipsum, fermentum quis purus eget, ullamcorper aliquet leo. Sed a lacus sem. Nam pulvinar augue vitae dui iaculis, auctor mollis sem ultrices. Nam cursus consequat tincidunt. Phasellus pharetra pretium nibh non laoreet. Etiam id feugiat urna. Sed malesuada turpis augue, sed sollicitudin quam viverra tincidunt. Duis sit amet mauris tempor risus gravida rhoncus.</p>
      <p>Ut scelerisque viverra ligula, ut euismod lectus varius eget. Maecenas non pharetra neque. Suspendisse potenti. Donec eget mauris et ligula ullamcorper laoreet. Donec tristique dapibus lacus, nec blandit dui dignissim pharetra. Maecenas vulputate est eget blandit euismod. Sed et dolor venenatis, tempus lorem in, aliquet metus. Nunc eu orci vel metus molestie porta.</p>
      <p class="sign-off">Regards,<br>Your Name<br>Designation</p>
    </section>

    <footer class="footer-band">
      <span class="grey"></span>
      <span class="blue"></span>
    </footer>
  </main>
</body>
</html>
```